Tamsin Vale Chiropractic Web Design

We need a fully operating Web site design INCLUDING the code for a Chiropractic Clinic based in Auckland New Zealand to target people from different financial backgrounds.

We need 4 Pages as followed:
1. Home: includes Slideshow of the clinic, General information about chiropractic, option for "Request an appointment", and it would be nice to have a picture on the top right side of the header and the clinic's name and logo on the top left side. on the bottom right we would like a small section for "Testimonial" (A good example: http://www.brindlemoorstudios.example/ )
(A good example for slide show is: http://www.pelvoro.example.nz/)
(A good example for the header is: http://www.spinehavenwelt.example.com/)

2. About Us: this section will include the background information of the company, and a section for our staff (which will includes a photo and description of each person/staff which can be changedanytime)
(a good example: http://www.fernwaybackcare.example.nz/)

3. Contact: includes location, map, contact numbers, email, and a contact box (A good example: http://www.brindlemoorstudios.example/contact/)

4. Services: includes our products, adjustment equipment, chiropractic products for sale, few pictures of patients while under chiropractic care/adjustment tables

We would also like to add "social networking" options on the bottom left side of every page (Facebook, twitter, Blog, Google+)

Please check the following links to get a feel of our favorite designs:
http://www.spinehavenwelt.example.com/
http://www.fernwaybackcare.example.nz/
http://www.pelvoro.example.nz/
http://www.dunmerespinalcentre.example.com/
http://www.quietbirch.example.nz/
http://www.pwo.example.nz/index-1.html
http://home.corelinespine.example.nz/home/

we would like to have full access to the back-end- admin of the website to be able to change and add any pictures or texts.
Updates

Hi Lovely Designer,

thank you so much for your proposed designs. We just uploaded the original source file of our logo, for you all to have access on it to facilitate your work. 

Enjoy your day

Leni

Target Market(s)

People with different financial background as well as we are located in the artistic part of town, so appealing to those crowd is important to us.

Industry/Entity Type

Financial

Requirements
Must have
• 1.color similar to the logo or darker colors (Dark and rich colors are prefered)
2. more artistic than a basic doctors' clinic
3. I would like the opening of the web to bring art, tranquility and peaceful images into mind
Should not have
• Not bombarded with lots of info and pics in one page, not too busy and crowded

```html
<!DOCTYPE html>
<html lang="en">
<head>
<meta charset="utf-8">
<title>Tamsin Vale Chiropractic</title>
<link href="https://fonts.googleapis.com/css2?family=Questrial&family=Arimo:ital,wght@0,400;1,400&family=Ubuntu:wght@500&display=swap" rel="stylesheet">
<style>
:root{
  --navy:#062a57;
  --navy-deep:#021f45;
  --navy-text:#0b2f5c;
  --lime:#8cc11b;
  --lime-dark:#5e9a0c;
  --lime-light:#b9e05a;
  --body-text:#333;
  --rule:#d4d4d4;
  --star:#f5862a;
  --footer-top:#2c2c2c;
  --footer-bottom:#141414;
  --footer-text:#9a9a9a;
}
*{margin:0;padding:0;box-sizing:border-box}
html,body{width:1112px;height:1200px;overflow:hidden}
body{position:relative;background:linear-gradient(#f1f1f1 436px,#fafafa 700px,#efefef 1097px);font-family:"Arimo",Arial,sans-serif;color:var(--body-text)}
.abs{position:absolute}
.header-band{left:0;top:0;width:1112px;height:436px;background:radial-gradient(ellipse at 50% 30%,#0a3468 0%,var(--navy) 55%,var(--navy-deep) 100%)}
.brand{left:107px;top:40px;display:flex;align-items:center;gap:12px}
.brand-mark{width:30px;height:30px;border-radius:50%;background:var(--lime)}
.brand-name{font-family:"Questrial",sans-serif;font-size:26px;line-height:30px;color:var(--lime-light);width:220px}
.nav{left:518px;top:58px;display:flex;align-items:center;font-family:"Questrial",sans-serif;font-size:17px;color:#fff}
.nav a{color:#fff;text-decoration:none}
.nav .current{background:var(--lime);border-radius:4px;padding:6px 16px;height:33px;line-height:21px}
.nav .item{padding:0 33px;border-left:1px solid #25497a;height:30px;line-height:30px}
.nav .sep-first{margin-left:31px}
.slider{left:100px;top:143px;width:913px;height:393px;background:#fff;box-shadow:0 14px 16px -10px rgba(0,0,0,.35)}
.slide-photo{left:6px;top:5px;width:901px;height:381px;background:linear-gradient(180deg,#8fb45a 0%,#6f9a3a 45%,#cfd6c0 70%,#9fbf6a 100%)}
.slide-caption{left:6px;top:79px;width:408px;height:48px;background:rgba(235,242,215,.75);font-family:"Questrial",sans-serif;font-size:28px;line-height:48px;padding-left:13px;color:#1c1c1c}
.arrow{width:64px;height:64px;border-radius:50%;background:#fff;box-shadow:0 0 6px rgba(0,0,0,.25)}
.arrow svg{position:absolute;top:22px}
.welcome{left:102px;top:570px;font-family:"Questrial",sans-serif;font-size:33px;color:var(--navy-text);display:flex;align-items:center;gap:12px}
.welcome .name{font-size:20px;color:#555;display:flex;align-items:center;gap:8px}
.welcome .dot{width:14px;height:14px;border-radius:50%;background:#666}
.appointment{left:785px;top:565px;width:214px;height:50px;border-radius:8px;background:linear-gradient(#b2dc3c,var(--lime) 50%,var(--lime-dark));border:1px solid #6a9e12;display:flex;align-items:center;padding-left:10px;gap:8px;color:#111}
.appointment .small{font-size:13px;line-height:14px;display:block}
.appointment .big{font-family:"Ubuntu",sans-serif;font-size:22px;line-height:24px;display:block;letter-spacing:.5px}
.welcome-rule{left:102px;top:624px;width:899px;height:1px;background:var(--rule)}
.intro{left:100px;top:645px;width:920px;font-size:13px;line-height:20.4px;letter-spacing:.1px}
.col-rule{top:813px;width:1px;height:253px;background:var(--rule)}
.col-title{font-family:"Questrial",sans-serif;font-size:26px;color:var(--navy-text)}
.thumb{width:259px;height:119px;background:#dcdcdc;padding:9px}
.thumb-fill{width:100%;height:100%;border:1px solid #fff}
.col-text{width:265px;font-size:12px;line-height:18.5px}
.learn{font-size:11px;font-style:italic;color:var(--lime-dark);text-align:right;width:257px}
.testimonial h3{font-family:"Ubuntu",sans-serif;font-weight:500;font-size:13px;color:#333;letter-spacing:.2px}
.testimonial .stars{margin-top:6px;display:flex;gap:2px}
.testimonial .date{font-size:11px;font-style:italic;color:var(--lime-dark);margin-top:3px}
.testimonial p{font-size:12px;line-height:13.5px;margin-top:5px;width:255px}
.testimonial-rule{left:739px;top:950px;width:255px;height:1px;background:#ddd}
.footer{left:0;top:1097px;width:1112px;height:103px;background:linear-gradient(var(--footer-top),var(--footer-bottom))}
.footer .brand{top:28px}
.footer .brand-name{color:#ddd;font-size:22px;line-height:26px;width:200px}
.footer .brand-mark{background:#ddd;width:26px;height:26px}
.talk{left:353px;top:1113px;display:flex;align-items:center;gap:14px;font-family:"Questrial",sans-serif;color:var(--footer-text)}
.talk .label{font-size:19px}
.talk .number{font-size:40px;letter-spacing:-1px}
.footer-rule{left:353px;top:1159px;width:454px;border-top:1px dotted #555}
.legal{left:357px;top:1178px;font-size:11px;color:var(--footer-text);letter-spacing:.3px}
.social{left:876px;top:1118px;display:flex;gap:4px}
.social span{width:30px;height:30px;border-radius:50%;background:#bdbdbd;display:block}
</style>
</head>
<body>
<div class="abs header-band"></div>

<div class="abs brand">
  <span class="brand-mark"></span>
  <span class="brand-name">Tamsin Vale Chiropractic</span>
</div>

<nav class="abs nav">
  <a class="current" href="#">Home</a>
  <a class="item sep-first" href="#">About Us</a>
  <a class="item" href="#">Contact Us</a>
  <a class="item" href="#">Services</a>
</nav>

<section class="abs slider">
  <div class="abs slide-photo" role="img" aria-label="Slideshow photo of a smiling family of four outdoors on a sunny green lawn"></div>
  <div class="abs slide-caption">Restoring Health To Your Body</div>
</section>
<div class="abs arrow" style="left:72px;top:300px">
  <svg style="left:28px" width="12" height="20" viewBox="0 0 12 20"><path d="M10 2 L3 10 L10 18" fill="none" stroke="var(--navy)" stroke-width="4"/></svg>
</div>
<div class="abs arrow" style="left:975px;top:308px">
  <svg style="left:22px" width="12" height="20" viewBox="0 0 12 20"><path d="M2 2 L9 10 L2 18" fill="none" stroke="var(--navy)" stroke-width="4"/></svg>
</div>

<div class="abs welcome">WELCOME TO <span class="name"><span class="dot"></span>Tamsin Vale Chiropractic</span></div>

<a class="abs appointment" href="#">
  <svg width="44" height="38" viewBox="0 0 44 38">
    <rect x="2" y="8" width="30" height="26" rx="2" fill="#111"/>
    <rect x="6" y="4" width="3" height="8" fill="#111"/><rect x="14" y="4" width="3" height="8" fill="#111"/><rect x="22" y="4" width="3" height="8" fill="#111"/>
    <g fill="#bfe36a"><rect x="6" y="16" width="4" height="3"/><rect x="12" y="16" width="4" height="3"/><rect x="18" y="16" width="4" height="3"/><rect x="6" y="22" width="4" height="3"/><rect x="12" y="22" width="4" height="3"/><rect x="6" y="28" width="4" height="3"/></g>
    <circle cx="32" cy="26" r="10" fill="#fff" stroke="#111" stroke-width="2.5"/>
    <path d="M32 20 V26 H37" fill="none" stroke="#111" stroke-width="2"/>
  </svg>
  <span><span class="small">Request an</span><span class="big">Appointment</span></span>
</a>
<div class="abs welcome-rule"></div>

<p class="abs intro">simply dummy text of the printing and typesetting industry. Lorem Ipsum has been the industry's standard dummy text ever since the 1500s, when an unknown printer took a galley of type and scrambled it to make a type specimen book. It has survived not only five centuries, but also the leap into electronic typesetting, remaining essentially unchanged. It was popularised in the 1960s with the release of standard dummy text ever since the 1500s, when an unknown printer took a galley of type and scrambled it to make a type specimen book. It has survived since the 1500s, when an unknown printer took a galley of type and scrambled it to make a type not only five centuries, but also the leap into electronic typesetting, remaining essentially unchanged. It was popularised Letraset sheets containing Lorem Ipsum passages.</p>

<div class="abs col-rule" style="left:399px"></div>
<div class="abs col-rule" style="left:712px"></div>

<section class="abs" style="left:112px;top:805px">
  <h2 class="col-title">Our Services</h2>
  <div class="thumb" style="margin-top:14px"><div class="thumb-fill" role="img" aria-label="Photo of a chiropractor's hands adjusting a patient's lower back" style="background:linear-gradient(90deg,#b07a63,#d9ae96 45%,#efe7e2)"></div></div>
  <p class="col-text" style="margin-top:12px;margin-left:2px">simply dummy text of the printing and typesetting industry. Lorem Ipsum has been the industry's standard dummy text ever since.</p>
  <p class="learn" style="margin-top:4px">Learn More »</p>
</section>

<section class="abs" style="left:427px;top:805px">
  <h2 class="col-title">Our Products</h2>
  <div class="thumb" style="margin-top:14px"><div class="thumb-fill" role="img" aria-label="Product photo of a black padded chiropractic adjustment table" style="background:linear-gradient(160deg,#fff 20%,#3a4a48 45%,#2a3432 60%,#e9e4da 80%,#fff)"></div></div>
  <p class="col-text" style="margin-top:12px;margin-left:2px">simply dummy text of the printing and typesetting industry. Lorem Ipsum has been the industry's standard dummy text ever since.</p>
  <p class="learn" style="margin-top:4px">Learn More »</p>
</section>

<h2 class="abs col-title" style="left:737px;top:807px">Clients Testimonials</h2>

<article class="abs testimonial" style="left:739px;top:853px">
  <h3>SIMPLY TEXT DUMMY TEXT THE PRINTING</h3>
  <div class="stars">
    <svg width="78" height="14" viewBox="0 0 78 14" fill="var(--star)"><g id="s"><polygon points="7,0 8.8,4.8 14,5 10,8.3 11.3,13.5 7,10.6 2.7,13.5 4,8.3 0,5 5.2,4.8"/></g><use href="#s" x="16"/><use href="#s" x="32"/><use href="#s" x="48"/><use href="#s" x="64"/></svg>
  </div>
  <p class="date">Wed, May 12, 2013</p>
  <p>simply dummy text of the printing and type sett ing Ipsum has industry....</p>
</article>
<div class="abs testimonial-rule"></div>
<article class="abs testimonial" style="left:739px;top:961px">
  <h3>SIMPLY TEXT DUMMY TEXT THE PRINTING</h3>
  <div class="stars">
    <svg width="78" height="14" viewBox="0 0 78 14" fill="var(--star)"><use href="#s"/><use href="#s" x="16"/><use href="#s" x="32"/><use href="#s" x="48"/><use href="#s" x="64"/></svg>
  </div>
  <p class="date">Wed, May 12, 2013</p>
  <p>simply dummy text of the printing and type sett ing Ipsum has industry....</p>
</article>

<footer class="abs footer">
  <div class="abs brand">
    <span class="brand-mark"></span>
    <span class="brand-name">Tamsin Vale Chiropractic</span>
  </div>
</footer>
<div class="abs talk">
  <span class="label">Talk to us!</span>
  <svg width="14" height="28" viewBox="0 0 14 28"><path d="M10 1 C3 2 1 8 1 14 C1 20 3 26 10 27 L12 20 L8 19 C6 16 6 12 8 9 L12 8 Z" fill="var(--footer-text)"/></svg>
  <span class="number">800 314 276</span>
</div>
<div class="abs footer-rule"></div>
<p class="abs legal">©2013. All rights reserved.&nbsp;&nbsp;&nbsp;Privacy Policy&nbsp;&nbsp;|&nbsp;&nbsp;Terms &amp; Conditions</p>
<div class="abs social" aria-label="Social links"><span></span><span></span><span></span><span></span></div>
</body>
</html>
```